Washing powder bag design.

Project Description – Graphic Design Proposal for ORBO Laundry Powder Packaging
We have already explored initial design ideas internally, supported by AI-assisted tools (ChatGPT) to develop early concepts, layouts, and mockups. To support this, we have attached the bag die-cut, where graphics and text are placed as a visual guideline for the intended structure. In addition, we have included a mockup of the product series currently under development to clearly communicate the desired style, direction, and overall visual identity.
The mockup should be regarded as the design foundation for this project and as a starting point for professional refinement.
Scope of Work
We would like you to create three graphic design variants, each based on a different color direction:
1. Variant 1: In line with our current color scheme
2. Variant 2: A blue version
3. Variant 3: A green version
Design Elements to Be Preserved
The following elements must be maintained across all three variants:
• The overall style and visual expression of the mockup
• The leaf-shaped element in the bottom right corner
• The ORBO layout, including typography, positioning, and general look & feel
Summary
While the color palette may vary, the structure, style, and key design elements must remain consistent and be directly based on the attached mockup.
We look forward to seeing your creative interpretation and professional input.
Updates
We need the design to be created based on the attached die-cut file “Orbo 10 kg BAG 202526”, including all text elements.
We would like the final to include both the designed die-cut file and a mockup.

```html
<!DOCTYPE html>
<html lang="da">
<head>
<meta charset="utf-8">
<title>ORBO Vaskepulver – 10 kg bag, back and front</title>
<link rel="stylesheet" href="https://fonts.googleapis.com/css2?family=Montserrat:wght@400;600;700;800&family=Open+Sans:wght@400;600;700&display=swap">
<style>
  :root{
    --bag-top:#e4eed9;
    --bag-bottom:#d5e4c6;
    --green-deep:#2f4a22;
    --green-dark:#3d5a2c;
    --green-stripe:#4c6b39;
    --green-mid:#86a85a;
    --green-light:#9ec27a;
    --green-pale:#cbe0b4;
    --green-ring:#dde9cf;
    --ink:#111;
    --white:#fff;
    --hazard:#d62020;
  }
  *{box-sizing:border-box;margin:0;padding:0}
  html,body{width:1200px;height:1200px;overflow:hidden;background:#fff}
  .canvas{position:relative;width:1200px;height:1200px;background:#fff;font-family:"Montserrat",sans-serif;color:var(--green-deep)}
  .bag{position:absolute;top:100px;width:540px;height:1000px;background:linear-gradient(180deg,var(--bag-top),var(--bag-bottom));border-radius:6px;overflow:hidden}
  .bag--back{left:40px}
  .bag--front{left:620px}
  .hang-hole{position:absolute;width:50px;height:50px;border-radius:50%;background:var(--white)}

  /* ---------- front ---------- */
  .leaf-deco{position:absolute;border-radius:50% 0 50% 0;background:linear-gradient(135deg,rgba(158,194,122,.28),rgba(158,194,122,.08))}
  .band{position:absolute;left:62px;top:0;width:398px;height:524px;border-radius:0 0 199px 199px;
        background:repeating-linear-gradient(90deg,var(--green-dark) 0 14px,var(--green-stripe) 14px 28px)}
  .emblem{position:absolute;left:86px;top:150px;width:350px;height:350px;border-radius:50%;background:var(--green-pale);border:5px solid var(--green-ring)}
  .sprig{position:absolute;left:80px;top:30px;width:180px;height:280px;border-radius:50%;
         background:radial-gradient(ellipse at center,rgba(134,168,90,.55),rgba(134,168,90,0) 70%)}
  .brand-name{position:absolute;left:0;top:276px;width:522px;text-align:center;font-weight:800;font-size:84px;line-height:90px;color:var(--green-deep);letter-spacing:1px}
  .product-title{position:absolute;left:0;top:548px;width:540px;text-align:center;font-weight:800;font-size:56px;line-height:60px;color:var(--green-deep)}
  .product-sub{position:absolute;left:0;top:608px;width:540px;text-align:center;font-weight:700;font-size:31px;line-height:34px;color:var(--green-mid)}
  .claim{position:absolute;left:85px;top:660px;width:352px;height:106px;border-radius:53px;background:var(--green-light);padding:6px}
  .claim__inner{width:100%;height:100%;border-radius:47px;background:var(--green-deep);color:var(--white);
                display:flex;align-items:center;justify-content:center;text-align:center;font-weight:700;font-size:27px;line-height:34px}
  .care-icons{position:absolute;display:flex}
  .care-tile{border-radius:14px;background:var(--green-deep);border:3px solid var(--green-light);display:flex;align-items:center;justify-content:center}
  .care-tile__inner{background:var(--white);border-radius:10px;display:flex;align-items:center;justify-content:center;font-weight:800;color:var(--green-deep)}
  .front-icons{left:20px;top:830px;gap:12px}
  .front-icons .care-tile{width:88px;height:92px}
  .front-icons .care-tile__inner{width:62px;height:62px;font-size:26px}
  .temps{position:absolute;font-weight:700;color:var(--green-deep);white-space:nowrap}
  .front-temps{left:22px;top:935px;font-size:22px}
  .weight-badge{position:absolute;left:374px;top:816px;width:132px;height:132px;border-radius:50%;background:var(--green-deep);border:7px solid var(--green-light);
                display:flex;align-items:center;justify-content:center;color:var(--white)}
  .weight-badge__num{font-weight:800;font-size:62px;letter-spacing:-4px}
  .weight-badge__unit{font-weight:800;font-size:22px;color:var(--green-light);margin-left:2px;margin-top:8px}

  /* ---------- back ---------- */
  .usage-panel{position:absolute;left:18px;top:197px;width:232px;height:757px;background:var(--white);border:2px solid var(--ink);border-radius:7px;overflow:hidden;
               font-family:"Open Sans",sans-serif;color:#222;font-size:6.8px;line-height:1.3;text-align:center}
  .usage-panel__head{background:var(--ink);color:var(--white);font-size:7px;font-weight:600;padding:4px 6px;text-align:left}
  .usage-panel__body{padding:7px 8px 5px}
  .usage-panel__body p{margin-bottom:5px}
  .warning-box{position:absolute;left:291px;top:193px;width:205px;height:300px;background:#f4f4f4;border:2px solid var(--ink);border-radius:7px;
               font-family:"Open Sans",sans-serif;font-size:5.6px;line-height:1.3;color:#222;text-align:center;padding:0 8px}
  .warning-box__tag{position:absolute;left:50%;top:-8px;transform:translateX(-50%);background:var(--ink);color:var(--white);font-size:7.5px;font-weight:700;padding:2px 8px;border-radius:3px;white-space:nowrap}
  .warning-box__pictogram{display:block;margin:26px auto 12px}
  .warning-box__ufi{position:absolute;left:0;bottom:4px;width:100%;font-size:5px}
  .dosage-title{position:absolute;left:288px;top:560px;width:200px;text-align:center;font-weight:800;font-size:29px;line-height:34px;color:var(--green-deep)}
  .dosage-table{position:absolute;left:286px;top:653px;width:204px;border-collapse:collapse;color:var(--green-deep);font-size:8px;text-align:center}
  .dosage-table td,.dosage-table th{border:1.5px solid var(--green-deep);padding:2px 1px;font-weight:600}
  .dosage-table th{font-size:8px}
  .dosage-table .row-label{font-size:15px;font-weight:700;width:66px}
  .back-icons{left:288px;top:876px;gap:10px}
  .back-icons .care-tile{width:60px;height:62px;border-radius:10px}
  .back-icons .care-tile__inner{width:42px;height:42px;font-size:17px;border-radius:7px}
  .back-temps{left:288px;top:946px;font-size:12.5px}
</style>
</head>
<body>
<div class="canvas">

  <!-- Back panel -->
  <section class="bag bag--back" aria-label="Back of bag">
    <span class="hang-hole" style="left:168px;top:55px"></span>
    <span class="hang-hole" style="left:245px;top:55px"></span>
    <span class="hang-hole" style="left:323px;top:55px"></span>

    <div class="usage-panel">
      <div class="usage-panel__head">(DK) BRUGERVEJLEDNING – ORBO VASKEPULVER</div>
      <div class="usage-panel__body">
        <p>Til universel brug.<br>Egnet til alle typer af vaskemaskiner og alle vaskbare tekstiler. Effektiv fra 20°C til 90°C. Udviklet til både kulørt og hvidt tøj. Fjerner snavs, fedt og lugt og efterlader tekstilerne rene og friske.</p>
        <p>Brugsanvisning:<br>Sorter tøjet efter farve og tekstiltype. Følg altid vaskeanvisningen i tøjet. Fyld vaskemaskinen korrekt – overfyldning reducerer vaskeevnen. Doser efter vandhårdhed, mængde og tilsmudsning. Hæld pulveret i doseringsskuffen eller direkte i tromlen (i egnet dosisbeholder). Brug mindre dosering til let snavset vasketøj og blødt vand.</p>
        <p>Anbefalinger:<br>• Undgå overdosis – det beskytter både miljø og maskine.<br>• Ved meget hårdt vand kan ekstra dosering være nødvendig.<br>• Ved vanskelige pletter anbefales forbehandling.<br>• Velegnet til septiktanke ved korrekt dosering.</p>
        <p>Opbevaring:<br>Opbevares tørt og tæt lukket.<br>Beskyt mod fugt. Må ikke udsættes for direkte sollys.<br>Opbevares utilgængeligt for børn.</p>
        <p>Sikkerhed:<br>Forårsager alvorlig øjenirritation og kan forårsage hudirritation. Undgå kontakt med øjne og hud. VED KONTAKT MED ØJNENE: Skyl forsigtigt med vand i flere minutter. Fjern kontaktlinser, hvis det er muligt. VED KONTAKT MED HUDEN: Skyl med vand. Sikkerhedsdatablad kan rekvireres efter anmodning.</p>
        <p>Ingredienser (EF 648/2004):<br>Anioniske tensider, nonioniske tensider, zeolitter, polycarboxylater, enzymer (amylase, protease), optisk hvidt, parfume.</p>
      </div>
      <div class="usage-panel__head">(GB) USER GUIDE – ORBO LAUNDRY DETERGENT POWDER</div>
      <div class="usage-panel__body">
        <p>Universal detergent.<br>Suitable for all types of washing machines and all washable textiles. Effective from 20°C to 90°C. Designed for both coloured and white laundry. Removes dirt, grease and odours, leaving fabrics clean and fresh.</p>
        <p>Instructions for use:<br>Sort laundry by colour and fabric type. Always follow the garment care labels. Load the machine correctly – overloading reduces washing performance. Dose according to water hardness, soil level and load size. Add detergent into the dispenser drawer or directly into the drum using a dosing ball. Use a reduced dosage for lightly soiled laundry and soft water.</p>
        <p>Recommendations:<br>• Avoid overdosing – helps protect both the environment and your machine.<br>• For very hard water, additional detergent may be required.<br>• For stubborn stains, pre-treatment is recommended.<br>• Suitable for septic tanks when used as directed.</p>
        <p>Storage:<br>Store in a dry place with the bag tightly closed. Protect from moisture. Do not expose to direct sunlight. Keep out of reach of children.</p>
        <p>Safety:<br>Causes serious eye irritation and may cause skin irritation. Avoid contact with eyes and skin. IF IN EYES: Rinse cautiously with water for several minutes. Remove contact lenses if possible. IF ON SKIN: Rinse with water. Safety data sheet available on request.</p>
        <p>Ingredients (EC 648/2004):<br>Anionic surfactants, non-ionic surfactants, zeolites, polycarboxylates, enzymes (amylase, protease), optical brightener, perfume.</p>
      </div>
    </div>

    <div class="warning-box">
      <span class="warning-box__tag">Advarsel Warning</span>
      <svg class="warning-box__pictogram" width="74" height="74" viewBox="0 0 74 74" aria-label="Hazard pictogram">
        <rect x="15" y="15" width="44" height="44" transform="rotate(45 37 37)" fill="#fff" stroke="var(--hazard)" stroke-width="5"/>
        <rect x="33.5" y="19" width="7" height="25" rx="3" fill="#111"/>
        <circle cx="37" cy="52" r="4" fill="#111"/>
      </svg>
      <p><b>(DK)</b> Forårsager hudirritation. Forårsager alvorlig øjenirritation. Indeholder subtilisin, amylase, alpha, parfume. Kan udløse allergisk reaktion. Sikkerhedsdatablad kan på anmodning rekvireres. Hvis der er brug for lægehjælp, medbring da beholderen eller etiketten. Opbevares utilgængeligt for børn. Vask hænder grundigt efter brug. Bær beskyttelseshandsker. VED KONTAKT MED ØJNENE: Skyl forsigtigt med vand i flere minutter. Fjern eventuelle kontaktlinser. Ved vedvarende øjenirritation: Søg lægehjælp.</p>
      <p style="margin-top:4px"><b>(GB)</b> Causes skin irritation. Causes serious eye irritation. Contains subtilisin, amylase, perfume. May produce an allergic reaction. Safety data sheet available on request. If medical advice is needed, have product container or label at hand. Keep out of reach of children. Wash hands thoroughly after handling. Wear eye protection/face protection/protective gloves. IF IN EYES: Rinse cautiously with water for several minutes. Remove contact lenses, if present and easy to do. Continue rinsing. If eye irritation persists: Get medical advice/attention.</p>
      <p class="warning-box__ufi">UFI: A3K0-P7WQ-2N9R-H6TD</p>
    </div>

    <h2 class="dosage-title">DOSERING<br>DOSAGE</h2>
    <table class="dosage-table">
      <tr><th></th><th>soft</th><th>medium</th><th>hard</th></tr>
      <tr><td class="row-label">1Kg</td><td>37 ml<br>=41g</td><td>37 ml<br>=61g</td><td>83 g</td></tr>
      <tr><td class="row-label">5Kg</td><td>65 Kg</td><td>37 ml<br>=83g</td><td>83 g</td></tr>
      <tr><td class="row-label">10Kg</td><td>112 Kg</td><td>112 ml<br>=124g</td><td>144g</td></tr>
      <tr><td></td><td colspan="3">75 ml = 83g</td></tr>
    </table>

    <div class="care-icons back-icons">
      <div class="care-tile"><div class="care-tile__inner">120</div></div>
      <div class="care-tile"><div class="care-tile__inner">
        <svg width="26" height="26" viewBox="0 0 26 26" aria-label="Machine wash"><circle cx="13" cy="13" r="10" fill="none" stroke="var(--green-deep)" stroke-width="3"/><circle cx="13" cy="13" r="6" fill="var(--green-deep)"/></svg>
      </div></div>
      <div class="care-tile">
        <svg width="40" height="36" viewBox="0 0 40 36" aria-label="Hand wash"><path d="M4 16 H36 L32 32 H8 Z" fill="none" stroke="#fff" stroke-width="2"/><path d="M12 18 C14 8 22 6 28 4" fill="none" stroke="#fff" stroke-width="2" stroke-linecap="round"/></svg>
      </div>
    </div>
    <div class="temps back-temps">20°C | 30°C | 40°C | 60°C | 90°C</div>
  </section>

  <!-- Front panel -->
  <section class="bag bag--front" aria-label="Front of bag">
    <div class="leaf-deco" role="img" aria-label="Faint leaf illustration" style="left:-20px;top:260px;width:90px;height:190px"></div>
    <div class="leaf-deco" role="img" aria-label="Faint leaf illustration" style="left:450px;top:420px;width:110px;height:200px"></div>
    <div class="leaf-deco" role="img" aria-label="Large faint leaf illustration in the bottom right corner" style="left:330px;top:740px;width:230px;height:270px"></div>

    <div class="band"></div>
    <span class="hang-hole" style="left:165px;top:56px"></span>
    <span class="hang-hole" style="left:243px;top:56px"></span>
    <span class="hang-hole" style="left:323px;top:56px"></span>

    <div class="emblem">
      <div class="sprig" role="img" aria-label="Green leafy sprig illustration"></div>
    </div>
    <h1 class="brand-name">ORBO</h1>

    <h2 class="product-title">VASKEPULVER</h2>
    <p class="product-sub">LAUNDRY DETERGENT</p>

    <div class="claim"><div class="claim__inner">RENT OG FRISK<br>HVER EN DAG</div></div>

    <div class="care-icons front-icons">
      <div class="care-tile"><div class="care-tile__inner">120</div></div>
      <div class="care-tile"><div class="care-tile__inner">
        <svg width="40" height="40" viewBox="0 0 40 40" aria-label="Machine wash"><circle cx="20" cy="20" r="15" fill="none" stroke="var(--green-deep)" stroke-width="4"/><circle cx="20" cy="20" r="9" fill="var(--green-deep)"/></svg>
      </div></div>
      <div class="care-tile">
        <svg width="60" height="54" viewBox="0 0 40 36" aria-label="Hand wash"><path d="M4 16 H36 L32 32 H8 Z" fill="none" stroke="#fff" stroke-width="2"/><path d="M12 18 C14 8 22 6 28 4" fill="none" stroke="#fff" stroke-width="2" stroke-linecap="round"/></svg>
      </div>
    </div>
    <div class="temps front-temps">20°C | 30°C | 40°C | 60°C | 90°C</div>

    <div class="weight-badge"><span class="weight-badge__num">10</span><span class="weight-badge__unit">kg</span></div>
  </section>

</div>
</body>
</html>
```